Need a Web Site Design - Fresh, Modern, and Visually Engaging Website Design

I’m looking to create a clean, modern, and visually appealing website that effectively represents our brand and services. The design should focus on user experience, intuitive navigation, and a professional aesthetic.

The Home page should set the tone for the entire site, featuring a sleek, modern layout with strong visual appeal.

Our Company Logo colors attached. The design can incorporate this color theme or use a unique palette that complements it.

Site Map:
We will begin with the following sections, with the potential to expand and add more services in the future:

Home: A welcoming and engaging introduction to our business, highlighting key services and industries we serve.
About Us: Share our story, mission, and values to connect with visitors.
Software Development: Showcase our expertise in developing innovative software solutions.
Industries We Serve: Provide detailed insights into the sectors we specialize in, including:
- Payroll Sector
- Education
- Transportation
- Home Care Services
Contact Us: Offer easy ways for clients to reach out, including forms and contact details.
Footer: Include essential links, social media handles, and company details.

Draft content for Services Page
Services
We specialize in delivering tailored solutions to meet your business needs. Our expertise spans Product Development, App Development, and Website Development.

1. Product Development
From concept to completion, we help you bring innovative products to life.
What We Offer:
• Custom Software Solutions: Scalable and secure software tailored to your business processes.
• Prototyping & MVP Development: Rapid prototyping and Minimum Viable Product creation to validate ideas.
• End-to-End Development: Comprehensive support from ideation to launch.
• Integration Services: Seamless integration of new products with your existing systems.

2. App Development
Build cutting-edge mobile and desktop applications to engage your audience and enhance operational efficiency.
What We Offer:
• Native & Cross-Platform Apps: Applications built for iOS, Android, and cross-platform frameworks.
• User-Centered Design: Apps designed with intuitive interfaces and smooth user experiences.
• Custom Features: Tailored functionality to meet your unique business needs.
• Maintenance & Updates: Continuous support to keep your app relevant and high-performing.

3. Website Development
Your website is the face of your business. We ensure it leaves a lasting impression.
What We Offer:
• Custom Website Design: Unique and responsive designs tailored to your brand identity.
• E-Commerce Development: Scalable and secure online stores to grow your business.
• CMS Integration: Easy-to-manage content systems like WordPress, Joomla, or custom CMS.
• SEO Optimization: Built-in search engine optimization for enhanced visibility.

Your Journey with Us
Our streamlined approach ensures that your project is handled with precision, creativity, and care. We partner with you at every step to create tailored solutions that transform your business.

Phase One: Discovery
We start by understanding your business inside and out, ensuring the foundation for our partnership is built on knowledge and alignment.
Assessment & Analysis
We dive deep into your business environment to uncover challenges, identify growth opportunities, and understand the economic factors driving your operations.
Process Evaluation
Our team analyzes your current workflows and processes, identifying inefficiencies and areas where improvements can enhance productivity and effectiveness.
Data-Driven Strategy
Using your organization’s technical and operational data, we create informed strategies that align with your goals and drive meaningful outcomes.

Phase Two: Estimate
We present a fully customized solution tailored to your needs, empowering you with the information required to make confident decisions.
Technology Plan & Roadmap
We design a detailed technology roadmap that includes the functionalities you need, the ideal tools and technologies, and a timeline for project completion.
Transition Planning
Our scope includes planning for a seamless transition, covering everything from system migration to user training and long-term usability.
Future Forecasting
Our solutions are built to grow with your business. We consider scalability, future technology trends, and your organization’s long-term needs to ensure lasting success.

Phase Three: Blueprint
Every successful project begins with a comprehensive plan. Our blueprints define every aspect of functionality, technology, and user experience, ensuring a smooth path forward.
Technology and Architecture
We develop a detailed framework outlining the infrastructure, external integrations, security measures, and scalability plans for the project.
Interactive Prototype
We create a clickable prototype that showcases the design, user interface, and functionality of the system, ensuring alignment with your vision.
Engineering & Testing Plan
Our strategy includes step-by-step engineering and rigorous testing for quality, security, and scalability throughout the development process.
Risk Management
We anticipate potential risks and outline mitigation strategies, reducing surprises and keeping the project on track.

Phase Four: Engineering
Our team of expert software engineers transforms the blueprint into a robust, scalable system tailored to your needs.
Full-Service Teams
We assemble a specialized team for your project, ensuring the skills and expertise align with your business goals and technical requirements.
Strategic Delivery
Our phased development approach delivers essential features first, reducing risks and enabling faster time-to-market.
Close Collaboration with Clients
We keep you informed and involved through every sprint, ensuring your vision is realized from the MVP to the final release.

Phase Five: Training & Support
We ensure a smooth integration of your new software, provide training for your team, and offer ongoing support to guarantee success.
Smooth Transition
We work with you to test new modules, retire outdated systems, and ensure a seamless rollout of the new solution.
Teamwide Training
Our team provides comprehensive training, gathers performance feedback, and optimizes the system for peak efficiency.
Long-Term Support
We continue to refine and improve the system post-launch, introducing enhancements to keep you ahead of the curve.

Our Projects
Explore our portfolio of completed projects, each showcasing our commitment to excellence and innovation.
(Provide a visually appealing UI design to display the project list, such as tiles or cards featuring images, project names, and a brief description.)

```html
<!DOCTYPE html>
<html lang="en">
<head>
<meta charset="utf-8">
<title>Novaloom — Tailored Software Solutions</title>
<link rel="stylesheet" href="https://fonts.googleapis.com/css2?family=Urbanist:wght@600;700;800&family=Poppins:wght@400;500;600&display=swap">
<style>
:root{
  --navy:#120a3e;
  --blue:#0a6cf0;
  --cyan:#00a9e8;
  --green:#a6cf2b;
  --orange:#f15a2b;
  --ink:#2b2b2b;
  --muted:#6c6c7a;
  --white:#ffffff;
  --sky-a:#dff6fd;
  --sky-b:#e7e6fb;
  --field:#ffffff;
}
*{margin:0;padding:0;box-sizing:border-box}
html,body{width:1200px;height:4737px;overflow:hidden}
body{position:relative;background:var(--white);font-family:"Poppins",sans-serif;color:var(--ink)}
.abs{position:absolute}
h1,h2,h3,.logo{font-family:"Urbanist",sans-serif;font-weight:800}
.logo{font-size:26px;letter-spacing:.5px;color:var(--white)}

/* hero */
.hero{left:0;top:0;width:1200px;height:720px;background:var(--navy);overflow:hidden}
.blob-left{left:-140px;top:190px;width:560px;height:520px;border-radius:50%;background:radial-gradient(circle at 60% 40%,#3fb6ff 0%,#1e57f0 30%,rgba(30,40,160,.35) 55%,rgba(18,10,62,0) 70%)}
.blob-right{left:930px;top:40px;width:320px;height:440px;border-radius:46% 54% 40% 60%;background:radial-gradient(circle at 45% 40%,#49e0ff 0%,#1f8bff 35%,#3a2bd8 60%,rgba(18,10,62,0) 75%)}
.nav{left:52px;top:32px;width:1096px;height:30px}
.nav .logo{position:absolute;left:0;top:0}
.nav ul{position:absolute;left:325px;top:5px;display:flex;gap:30px;list-style:none}
.nav li{font-size:14px;color:#e8e6f6}
.btn{display:inline-flex;align-items:center;justify-content:center;border-radius:30px;font-family:"Poppins",sans-serif;font-weight:600;font-size:11px}
.btn-contact{left:1021px;top:27px;width:128px;height:38px;background:var(--white);color:var(--navy)}
.hero-title{left:0;top:218px;width:1200px;text-align:center;color:var(--white);font-size:50px;line-height:62px}
.hero-text{left:320px;top:352px;width:560px;text-align:center;color:#d7d4ee;font-size:14px;line-height:23px}
.btn-start{left:480px;top:424px;width:128px;height:38px;background:var(--white);color:var(--navy)}
.watch{left:618px;top:431px;display:flex;align-items:center;gap:10px;color:var(--white);font-size:11px;font-weight:600}
.scroll{left:550px;top:578px;width:100px;text-align:center;color:var(--white);font-size:14px;font-weight:600}

/* about */
.art{border-radius:24px}
.about-art{left:120px;top:827px;width:376px;height:505px;background:linear-gradient(160deg,#8f86ea,#6c63d9 45%,#f6a23c 80%,#e8e8ee)}
.sec-title{font-size:48px;color:var(--ink);line-height:56px}
.para{font-size:14px;line-height:23px;color:var(--muted)}
.btn-blue{background:var(--blue);color:var(--white)}

/* mission */
.mission-bg{left:0;top:1400px;width:1200px;height:1000px;background:linear-gradient(180deg,#ffffff 0%,var(--sky-a) 12%,#e9f8fd 60%,#ffffff 100%)}
.laptop-art{left:592px;top:1562px;width:492px;height:506px;background:linear-gradient(150deg,#3b5bdb,#2f46c7 45%,#d9dbe4 70%,#c9ccd6)}
.value{top:2110px;width:308px;height:244px;border-radius:10px;background:var(--white);box-shadow:0 12px 34px rgba(40,40,90,.08);padding:24px}
.value.dark{background:var(--navy)}
.value .ico{width:58px;height:58px;border-radius:10px;background:#f4f4f8}
.value.dark .ico{background:var(--cyan)}
.value h3{margin-top:26px;font-size:28px;color:var(--ink)}
.value.dark h3{color:var(--white)}
.value p{margin-top:10px;font-size:11px;line-height:19px;color:var(--muted);width:240px}
.value.dark p{color:#d2cfe8}

/* services */
.center{left:0;width:1200px;text-align:center}
.svc{top:2597px;width:312px;height:395px;border-radius:8px;padding:40px 44px;color:var(--white)}
.svc h3{font-size:30px;line-height:34px}
.svc .lead{margin-top:12px;font-size:11px;line-height:19px;opacity:.85}
.svc ul{list-style:none;margin-top:14px}
.svc li{font-size:11px;font-weight:600;line-height:28px;display:flex;align-items:center;gap:10px}
.svc li::before{content:"";width:11px;height:11px;border-radius:50%;background:var(--white);flex:none}
.svc .btn{margin-top:18px;width:126px;height:37px;background:var(--white);color:var(--ink)}

/* industries */
.ind{top:3240px;width:260px;text-align:center}
.ind .ico{width:88px;height:88px;margin:0 auto;border-radius:12px;background:#f3f4f8}
.ind h3{margin-top:28px;font-size:30px;color:var(--ink)}
.ind p{margin-top:10px;font-size:11px;line-height:18px;color:var(--muted)}

/* contact */
.contact-bg{left:0;top:3480px;width:1200px;height:808px;background:linear-gradient(180deg,#ffffff 0%,rgba(255,255,255,0) 14%),linear-gradient(135deg,var(--sky-a),var(--sky-b))}
.field{height:61px;border-radius:14px;background:var(--field);font-size:11px;color:#9a9aa8;padding:22px 18px}
.field.msg{height:158px}
.btn-submit{left:215px;top:4167px;width:127px;height:37px}

/* footer */
.footer{left:0;top:4288px;width:1200px;height:449px;background:var(--navy);overflow:hidden}
.foot-glow{left:-60px;top:300px;width:300px;height:240px;border-radius:50%;background:radial-gradient(circle,#2f6cff 0%,#2a3fd6 40%,rgba(18,10,62,0) 70%)}
.footer .logo{left:92px;top:112px}
.foot-about{left:92px;top:156px;width:285px;font-size:13px;line-height:23px;color:#dcd9f0}
.socials{left:92px;top:292px;display:flex;gap:12px}
.socials span{width:24px;height:24px;border-radius:50%;border:2px solid var(--white)}
.fcol{top:112px}
.fcol h4{font-family:"Urbanist",sans-serif;font-weight:700;font-size:20px;color:var(--white)}
.fcol ul{list-style:none;margin-top:16px}
.fcol li{font-size:13px;line-height:39px;color:#dcd9f0}
.vline{top:110px;width:1px;height:210px;background:rgba(255,255,255,.25)}
.hline{left:52px;top:381px;width:1096px;height:1px;background:rgba(255,255,255,.25)}
.fbottom{top:402px;font-size:12px;color:#dcd9f0}
</style>
</head>
<body>

<!-- HERO -->
<section class="abs hero">
  <div class="abs blob-left" role="img" aria-label="Soft blue glowing abstract shape"></div>
  <div class="abs blob-right" role="img" aria-label="Soft cyan and violet glowing abstract shape"></div>
  <nav class="abs nav">
    <div class="logo">NOVALOOM</div>
    <ul><li>Home</li><li>About Us</li><li>Services</li><li>Discovery</li><li>Training &amp; Support</li></ul>
  </nav>
  <div class="abs btn btn-contact">Contact Us</div>
  <h1 class="abs hero-title">Empowering Businesses With<br>Tailored Software Solutions!</h1>
  <p class="abs hero-text">Lorem Ipsum Dolor Sit Amet, Consectetur Adipiscing Elit, Sed Do Eiusmod Tempor Incididunt Ut Labore Et Dolore Magna Aliqua.</p>
  <div class="abs btn btn-start">Get Started</div>
  <div class="abs watch">
    <svg width="24" height="24" viewBox="0 0 24 24"><circle cx="12" cy="12" r="10" fill="none" stroke="#fff" stroke-width="2"/><path d="M10 8l6 4-6 4z" fill="#fff"/></svg>
    Watch Video
  </div>
  <div class="abs scroll">
    <svg width="24" height="36" viewBox="0 0 24 36"><rect x="2" y="2" width="20" height="32" rx="10" fill="none" stroke="#fff" stroke-width="2"/><line x1="12" y1="9" x2="12" y2="16" stroke="#fff" stroke-width="2" stroke-linecap="round"/></svg>
    <div style="margin-top:10px">Scroll down</div>
    <svg width="16" height="26" viewBox="0 0 16 26" style="margin-top:6px"><path d="M8 2v21M2 17l6 6 6-6" fill="none" stroke="#fff" stroke-width="1.8"/></svg>
  </div>
</section>

<!-- ABOUT -->
<div class="abs art about-art" role="img" aria-label="Isometric illustration of two developers placing code blocks into a large smartphone"></div>
<h2 class="abs sec-title" style="left:604px;top:862px">About Us</h2>
<p class="abs para" style="left:604px;top:933px;width:475px">Lorem Ipsum Dolor Sit Amet, Consectetur Adipiscing Elit, Sed Do Eiusmod Tempor Incididunt Ut Labore Et Dolore Magna Aliqua. Ut Enim Ad Minim Veniam, Quis Nostrud Exercitation Ullamco Laboris Nisi Ut Aliquip Ex Ea Commodo Consequat. Duis Aute Irure Dolor In Reprehenderit In Voluptate Velit Esse Cillum Dolore Eu Fugiat Nulla Pariatur. Excepteur Sint Occaecat Cupidatat Non Proident, Sunt In Culpa Qui Officia Deserunt Mollit Anim Id Est Laborum.</p>
<p class="abs para" style="left:604px;top:1138px;width:475px">Sed Ut Perspiciatis Unde Omnis Iste Natus Error Sit Voluptatem Accusantium Doloremque Laudantium, Totam Rem Aperiam, Eaque Ipsa Quae Ab Illo Inventore Veritatis Et Quasi Architecto Beatae Vitae Dicta Sunt Explicabo.</p>
<div class="abs btn btn-blue" style="left:604px;top:1256px;width:128px;height:37px">Learn More</div>

<!-- MISSION -->
<div class="abs mission-bg"></div>
<h2 class="abs sec-title" style="left:116px;top:1653px">Mission &amp; Vision</h2>
<p class="abs para" style="left:116px;top:1722px;width:470px">Lorem Ipsum Dolor Sit Amet, Consectetur Adipiscing Elit, Sed Do Eiusmod Tempor Incididunt Ut Labore Et Dolore Magna Aliqua. Ut Enim Ad Minim Veniam, Quis Nostrud Exercitation Ullamco Laboris Nisi Ut Aliquip Ex Ea Commodo Consequat. Duis Aute Irure Dolor In Reprehenderit In Voluptate Velit Esse Cillum Dolore Eu Fugiat Nulla Pariatur. Excepteur Sint Occaecat Cupidatat Non Proident, Sunt In Culpa Qui Officia Deserunt Mollit Anim Id Est Laborum.</p>
<div class="abs btn btn-blue" style="left:116px;top:1932px;width:128px;height:37px">Learn More</div>
<div class="abs art laptop-art" role="img" aria-label="Isometric illustration of a laptop with floating website and code windows"></div>

<div class="abs value dark" style="left:120px"><div class="ico" role="img" aria-label="Light bulb icon"></div><h3>Innovation</h3><p>We Thrive On Creating Cutting-Edge Solutions That Drive Progress And Deliver Exceptional Results.</p></div>
<div class="abs value" style="left:447px"><div class="ico" role="img" aria-label="Handshake and award icon"></div><h3>Collaboration</h3><p>Success Is A Partnership. We Work Closely With Clients To Bring Their Vision To Life.</p></div>
<div class="abs value" style="left:773px"><div class="ico" role="img" aria-label="Puzzle pieces icon"></div><h3>Integrity</h3><p>Trust And Transparency Guide Every Step Of Our Process.</p></div>

<!-- SOFTWARE DEVELOPMENT -->
<h2 class="abs sec-title center" style="top:2440px">Software Development</h2>
<p class="abs para center" style="top:2511px;padding:0 300px">Lorem Ipsum Dolor Sit Amet, Consectetur Adipiscing Elit, Sed Do Eiusmod Tempor Incididunt Ut Labore Et Dolore Magna Aliqua.</p>

<div class="abs svc" style="left:116px;background:var(--green)">
  <h3>Product<br>Development</h3>
  <p class="lead">From Concept To Completion, We Help You Bring Innovative Products To Life.</p>
  <ul><li>Custom Software Solutions</li><li>Prototyping &amp; MVP Development</li><li>End-To-End Development</li><li>Integration Services</li></ul>
  <div class="btn">Learn More</div>
</div>
<div class="abs svc" style="left:445px;background:var(--cyan);padding-top:32px">
  <h3>App<br>Development</h3>
  <p class="lead">Build Cutting-Edge Mobile And Desktop Applications To Engage Your Audience And Enhance Operational Efficiency.</p>
  <ul><li>Native &amp; Cross-Platform Apps</li><li>User-Centered Design</li><li>Custom Features</li><li>Maintenance &amp; Updates</li></ul>
  <div class="btn">Learn More</div>
</div>
<div class="abs svc" style="left:772px;background:var(--orange)">
  <h3>Website<br>Development</h3>
  <p class="lead">Your Website Is The Face Of Your Business. We Ensure It Leaves A Lasting Impression.</p>
  <ul><li>Custom Website Design</li><li>E-Commerce Development</li><li>CMS Integration</li><li>SEO Optimization</li></ul>
  <div class="btn">Learn More</div>
</div>

<!-- INDUSTRIES -->
<h2 class="abs sec-title center" style="top:3078px">Industries We Serve</h2>
<p class="abs para center" style="top:3149px;padding:0 300px">Lorem Ipsum Dolor Sit Amet, Consectetur Adipiscing Elit, Sed Do Eiusmod Tempor Incididunt Ut Labore Et Dolore Magna Aliqua.</p>
<div class="abs ind" style="left:91px"><div class="ico" role="img" aria-label="Payroll icon with people and banknote"></div><h3>Payroll Sector</h3><p>Lorem Ipsum Dolor Sit Amet,<br>Consectetur Adipiscing Elit</p></div>
<div class="abs ind" style="left:344px"><div class="ico" role="img" aria-label="Education icon with books and graduation cap"></div><h3>Education</h3><p>Lorem Ipsum Dolor Sit Amet,<br>Consectetur Adipiscing Elit</p></div>
<div class="abs ind" style="left:596px"><div class="ico" role="img" aria-label="Transportation icon with vehicles"></div><h3>Transportation</h3><p>Lorem Ipsum Dolor Sit Amet,<br>Consectetur Adipiscing Elit</p></div>
<div class="abs ind" style="left:848px"><div class="ico" role="img" aria-label="Home care icon with hands and heart"></div><h3>Home Care</h3><p>Lorem Ipsum Dolor Sit Amet,<br>Consectetur Adipiscing Elit</p></div>

<!-- CONTACT -->
<div class="abs contact-bg"></div>
<h2 class="abs sec-title center" style="top:3650px">Contact Us</h2>
<p class="abs para center" style="top:3720px;padding:0 370px">Lorem Ipsum Dolor Sit Amet, Consectetur Adipiscing Elit, Sed Do Eiusmod Tempor Incididunt Ut</p>
<div class="abs field" style="left:215px;top:3810px;width:239px">First Name</div>
<div class="abs field" style="left:480px;top:3810px;width:239px">Last Name</div>
<div class="abs field" style="left:744px;top:3810px;width:241px">Industry</div>
<div class="abs field" style="left:215px;top:3897px;width:373px">Contact No</div>
<div class="abs field" style="left:612px;top:3897px;width:373px">Email Address</div>
<div class="abs field msg" style="left:215px;top:3983px;width:770px">Message</div>
<div class="abs btn btn-blue btn-submit">Submit</div>

<!-- FOOTER -->
<footer class="abs footer">
  <div class="abs foot-glow" role="img" aria-label="Soft blue glow"></div>
  <div class="abs logo">NOVALOOM</div>
  <p class="abs foot-about">Lorem Ipsum Dolor Sit Amet, Consectetur Adipiscing Elit, Sed Do Eiusmod Tempor Incididunt Ut Labore Et Dolore Magna Aliqua.</p>
  <div class="abs socials" aria-label="Social media links"><span></span><span></span><span></span><span></span></div>
  <div class="abs fcol" style="left:452px"><h4>Get Started</h4><ul><li>Home</li><li>About Us</li><li>Services</li><li>Discovery</li><li>Training &amp; Support</li></ul></div>
  <div class="abs vline" style="left:640px"></div>
  <div class="abs fcol" style="left:693px"><h4>Quick Links</h4><ul><li>Career</li><li>Support</li><li>Terms &amp; Conditions</li><li>Privacy Policy</li><li>Help</li></ul></div>
  <div class="abs vline" style="left:880px"></div>
  <div class="abs fcol" style="left:934px"><h4>Services</h4><ul><li>App Development</li><li>Website Development</li><li>Product Development</li></ul></div>
  <div class="abs hline"></div>
  <div class="abs fbottom" style="left:52px">Terms &amp; Conditions</div>
  <div class="abs fbottom" style="left:0;width:1200px;text-align:center">© Novaloom All Rights Reserved.</div>
  <div class="abs fbottom" style="left:1051px">Privacy Policy</div>
</footer>

</body>
</html>
```